Permanent Makeup (cosmetics salon) Brochure

We need a 2-4 sites brochure for our Permanent Makeup (cosmetics salon). Our company is based in Austria / Vienna. -> Our homepage is www.mk-lorenzhuber.at
This brochure should show which treatments we provide ot our customers.

I've uploaded our old brochure, the content (text) would be nearly the same (look form "Must Haves", pics have to be new (look uploaded pics)
The old brochure is to dark. -> look for our homepage maybe you can make it like this

Target Market(s)

woman, age 25-70 years who wants to have permanent makeup on eyebrows, lips or eyeliner

Industry/Entity Type

Beauty Salon

Requirements
Must have
• pics which are uploaded.

*This text (somithing about our business)
"Für Frau Lorenzhuber ist Permanent Makeup ein Kunsthandwerk. Das Team von MK-Lorenzhuber ist spezialisiert auf natürliches Permanent Makeup damit der individuelle Typ jeder Kundin am schönsten zum Ausdruck kommt."

*We do this treatments: (english)
+ Augenbrauen Microblading (eyebrows)
+ Augenbrauen Permanent Makeup (eyebrows2)
+ Lidstrich Permanent Makeup (eyeliner)
+ Lip Blushing (lips)
+ Lippen Permanent Makeup (lips2)

* Our addresses (2 locations)
Wien
Kerngasse 7b/12, 1010 Wien
Tel: 01/5827316

Villach
Birkenhofweg 24, 9524 St. Ulrich
Tel: 0676/3158940

Mail: info@mk-lorenzhuber.at
www.mk-lorenzhuber.at

```html
<!DOCTYPE html>
<html lang="de">
<head>
<meta charset="utf-8">
<title>Broschüre – MK-Lorenzhuber Permanent Makeup</title>
<link rel="stylesheet" href="https://fonts.googleapis.com/css2?family=Oswald:wght@300;400&family=Montserrat:wght@300;500;600&display=swap">
<style>
  :root {
    --stage: #2a2a2a;
    --paper: #f3f3f4;
    --paper-shade: #e6e6e8;
    --headline: #66798b;
    --headline-strong: #4e6275;
    --band: #555557;
    --pill: #58585a;
    --pill-text: #f4f4f4;
    --ink: #3a3a3c;
    --gold: #c9a64a;
    --skin-light: #edcdb9;
    --skin: #dcae96;
    --skin-deep: #c48f78;
    --backdrop: #7f909d;
  }
  * { margin: 0; padding: 0; box-sizing: border-box; }
  html, body {
    width: 1200px; height: 768px; overflow: hidden;
    background: var(--stage);
  }
  .stage {
    width: 1200px; height: 768px;
    display: flex; align-items: center; justify-content: center;
  }
  .cover {
    position: relative;
    width: 700px; height: 700px;
    background: linear-gradient(135deg, var(--paper) 0%, #ffffff 45%, var(--paper-shade) 100%);
    overflow: hidden;
  }
  .cover-art {
    position: absolute; inset: 0;
    width: 700px; height: 700px;
  }
  .headline {
    position: absolute;
    left: 72px; top: 150px;
    font-family: "Oswald", sans-serif;
    font-weight: 300;
    color: var(--headline);
    line-height: 1.0;
  }
  .headline-line { display: block; font-size: 54px; letter-spacing: 0.5px; white-space: nowrap; }
  .headline-line.indent-1 { padding-left: 22px; }
  .headline-line.indent-2 { padding-left: 42px; }
  .headline-line.indent-3 { padding-left: 60px; }
  .headline-accent {
    display: block;
    font-size: 118px;
    line-height: 0.95;
    padding-left: 76px;
    color: var(--headline-strong);
    white-space: nowrap;
  }
  .brand {
    position: absolute;
    left: 100px; top: 560px;
    width: 380px;
    text-align: center;
    font-family: "Montserrat", sans-serif;
    color: var(--ink);
  }
  .brand-name {
    display: flex; align-items: center; justify-content: center; gap: 10px;
    font-weight: 500;
    font-size: 19px;
    letter-spacing: 0.5px;
    white-space: nowrap;
  }
  .brand-dot {
    width: 20px; height: 20px; border-radius: 50%;
    background: var(--gold);
    flex: none;
  }
  .brand-claim {
    margin-top: 7px;
    font-weight: 600;
    font-size: 8.5px;
    letter-spacing: 1.3px;
    text-transform: uppercase;
    white-space: nowrap;
  }
  .web-pill {
    position: absolute;
    left: 110px; top: 624px;
    width: 360px; height: 38px;
    border-radius: 19px;
    background: var(--pill);
    color: var(--pill-text);
    font-family: "Montserrat", sans-serif;
    font-weight: 300;
    font-size: 18px;
    letter-spacing: 0.6px;
    display: flex; align-items: center; justify-content: center;
    white-space: nowrap;
  }
</style>
</head>
<body>
  <main class="stage">
    <section class="cover">
      <svg class="cover-art" viewBox="0 0 700 700" xmlns="http://www.w3.org/2000/svg">
        <defs>
          <linearGradient id="portraitTones" x1="0" y1="0" x2="1" y2="1">
            <stop offset="0" stop-color="var(--skin-light)"/>
            <stop offset="0.45" stop-color="var(--skin)"/>
            <stop offset="0.75" stop-color="var(--skin-deep)"/>
            <stop offset="1" stop-color="var(--backdrop)"/>
          </linearGradient>
        </defs>
        <path class="wave-band" fill="var(--band)"
          d="M370,0 C330,80 330,170 400,260 C480,360 610,430 610,560 C610,630 592,670 582,700 L700,700 L700,0 Z"/>
        <path class="portrait" fill="url(#portraitTones)" role="img"
          aria-label="Porträtfoto einer Frau mit natürlichem Permanent Makeup an Augenbrauen und Lippen, Hand am Kinn"
          d="M398,0 C358,80 358,168 426,254 C506,354 638,424 638,556 C638,628 620,668 610,700 L700,700 L700,0 Z"/>
      </svg>

      <h1 class="headline">
        <span class="headline-line">Schönheit</span>
        <span class="headline-line indent-1">kommt</span>
        <span class="headline-line indent-2">nicht</span>
        <span class="headline-line indent-3">nur von</span>
        <span class="headline-accent">innen</span>
      </h1>

      <div class="brand">
        <div class="brand-name"><span class="brand-dot"></span>Marika Lorenzhuber</div>
        <p class="brand-claim">Was Ihnen wertvoll ist, gehört in gute Hände</p>
      </div>

      <div class="web-pill">www.mk-lorenzhuber.at</div>
    </section>
  </main>
</body>
</html>
```